NYC Counter Service restaurant needs menu to be featured on digital boards

Plate Haven NYC is a NEW counter-service restaurant in midtown NYC. We are looking to design 4 screens (16x9) to feature our menu. We had a ruff render we put up attached here (these are ugly, please don't work from that design). Feel free to visit our website (plateHavenNYC.example) for style direction-but overall we want a black, yellow, and white color scheme. We want one screen to be dedicated to the build your own bowl; and the other three can be distributed with other menu items at your discretion . Word doc attached has all menu items and prices. The picture will give you an idea of how they will look in store. We DO NOT want to feature photos of food on the boards. Only text. Sleek and cool design. Feel free to reach out with any questions.

Industry/Entity Type

Food Service

Colors
fbee3e
000000

Requirements
Must have
• 4 total screen assets all 16x9 - Menu distributed as follows: We want one screen to be dedicated to the build your own bowl; and the other three can be distributed with other menu items at your discretion.
Nice to have
• Nice modern feel, very sleek.
Should not have
• NO FOOD PHOTOS

```html
<!DOCTYPE html>
<html lang="en">
<head>
<meta charset="utf-8">
<title>Build Your Own Bowl</title>
<link href="https://fonts.googleapis.com/css2?family=Lobster+Two:ital,wght@1,700&family=Old+Standard+TT:wght@400&display=swap" rel="stylesheet">
<style>
  :root {
    --board-bg: #231f20;
    --accent-gold: #fcd20a;
    --wedge-olive: #8c7414;
    --text-light: #ffffff;
    --rule-grey: #8f8d8d;
  }
  * { margin: 0; padding: 0; box-sizing: border-box; }
  html, body { width: 1200px; height: 675px; overflow: hidden; background: var(--board-bg); }
  .menu-board {
    position: relative;
    width: 1200px;
    height: 675px;
    background: var(--board-bg);
    overflow: hidden;
    color: var(--text-light);
    font-family: "Old Standard TT", "Times New Roman", serif;
    text-align: center;
  }
  .accent-wedge { position: absolute; inset: 0; width: 1200px; height: 675px; }
  .board-title {
    position: absolute;
    top: 22px; left: 0; right: 0;
    font-family: "Lobster Two", cursive;
    font-style: italic;
    font-weight: 700;
    font-size: 70px;
    line-height: 1.2;
    color: var(--accent-gold);
  }
  .title-rule {
    position: absolute;
    top: 139px; left: 28px;
    width: 1144px; height: 1px;
    background: var(--rule-grey);
  }
  .menu-section {
    position: absolute;
    left: 40px; right: 40px;
  }
  .section-heading {
    font-family: "Lobster Two", cursive;
    font-style: italic;
    font-weight: 700;
    font-size: 28px;
    line-height: 1.2;
    color: var(--accent-gold);
    margin-bottom: 6px;
  }
  .section-items {
    font-size: 21px;
    line-height: 29px;
  }
  .section-base { top: 172px; }
  .section-protein { top: 270px; }
  .section-sides { top: 398px; }
  .section-sauces { top: 527px; }
</style>
</head>
<body>
<main class="menu-board">
  <svg class="accent-wedge" viewBox="0 0 1200 675" aria-hidden="true">
    <polygon points="1063,36 1200,118 1200,675 830,675 707,612" fill="var(--wedge-olive)"/>
  </svg>

  <h1 class="board-title">Build Your Own Bowl</h1>
  <div class="title-rule"></div>

  <section class="menu-section section-base">
    <h2 class="section-heading">Base</h2>
    <p class="section-items">Quinoa &nbsp;|&nbsp; Brown Rice &nbsp;|&nbsp; Spanish/ Veggie Rice &nbsp;|&nbsp; Mixed Greens &nbsp;|&nbsp; Couscous &nbsp;|&nbsp; Barley</p>
  </section>

  <section class="menu-section section-protein">
    <h2 class="section-heading">Protein</h2>
    <p class="section-items">Rotisserie Chicken &nbsp;|&nbsp; Rotisserie Turkey &nbsp;|&nbsp; Southwest London Broil &nbsp;|&nbsp; Caribbean Slow Roasted Pork Loin<br>Slow Roasted Brisket &nbsp;|&nbsp; Grilled Chicken &nbsp;|&nbsp; Chicken Strips &nbsp;|&nbsp; Tofu &nbsp;|&nbsp; Falafel &nbsp;|&nbsp; Grilled Norwegian Salmon</p>
  </section>

  <section class="menu-section section-sides">
    <h2 class="section-heading">Sides</h2>
    <p class="section-items">String Beans, Broccoli, Brussel Sprouts, Roasted Corn, Roasted Potatoes &nbsp;|&nbsp; Roasted Sweet Potatoes &nbsp;|&nbsp; Beet<br>Salad, Avocado Salad, Cucumber Tomatoes &nbsp;|&nbsp; Onion Salad</p>
  </section>

  <section class="menu-section section-sauces">
    <h2 class="section-heading">Sauces and Toppings</h2>
    <p class="section-items">Guacamole &nbsp;|&nbsp; Mango Salsa &nbsp;|&nbsp; Tzatziki Sauce &nbsp;|&nbsp; Hummus &nbsp;|&nbsp; Red Salsa| &nbsp;Caesar Dressing &nbsp;|&nbsp; Balsamic<br>Vinaigrette Dressing</p>
  </section>
</main>
</body>
</html>
```